Goodlooking website for a company who is working in the IT consultancy

We want a new website designed in WordPress. You can take www.vantorq.nl as an example. It should be a website with some short blocks of information about the company, nice pictures of our partners and our employees. A job page with a clear filter.

Target Market(s)

B2B

Industry/Entity Type

It Company

Coding

Coded - Design and coding required

Number of Pages Required

5+ page

Font styles to use
Sans Serif

Colors
0455a3
34a7d8

Requirements
Must have
• Check briefing

```html
<!DOCTYPE html>
<html lang="en">
<head>
<meta charset="utf-8">
<title>Quorvix – Core IT Systems</title>
<link href="https://fonts.googleapis.com/css2?family=Raleway:wght@400;500;600;700&family=Open+Sans:wght@400;600&display=swap" rel="stylesheet">
<style>
:root{
  --teal:#1fa3a5;
  --teal-dark:#0f5a66;
  --navy:#12303b;
  --ink:#1f2a30;
  --muted:#5c6870;
  --line:#d8dfe3;
  --footer:#151f27;
  --white:#ffffff;
}
*{box-sizing:border-box;margin:0;padding:0}
html,body{width:1200px;height:4380px;overflow:hidden}
body{position:relative;background:var(--white);font-family:"Open Sans",sans-serif;color:var(--ink)}
.abs{position:absolute}
h2.section-title{position:absolute;left:0;width:1200px;text-align:center;font-family:"Raleway",sans-serif;font-weight:600;font-size:28px;letter-spacing:1px;color:var(--ink)}
.intro{position:absolute;left:260px;width:680px;text-align:center;font-size:10.5px;line-height:21px;color:var(--muted)}
.btn{position:absolute;display:flex;align-items:center;justify-content:center;background:var(--teal);color:#fff;font-family:"Raleway",sans-serif;font-weight:700;font-size:11px;letter-spacing:.5px;border-radius:20px}

/* header */
.site-header{left:0;top:0;width:1200px;height:108px;background:#fff;border-top:4px solid var(--teal)}
.brand{display:flex;align-items:center;gap:12px}
.brand-mark{width:56px;height:56px;border-radius:50%;background:var(--teal-dark)}
.brand-name{font-family:"Raleway",sans-serif;font-weight:700;font-size:34px;letter-spacing:3px;color:var(--navy);line-height:1}
.brand-sub{font-family:"Raleway",sans-serif;font-size:9px;letter-spacing:2px;color:var(--teal);margin-top:4px}
.nav{left:622px;top:72px;display:flex;gap:38px;font-family:"Raleway",sans-serif;font-weight:600;font-size:12px;color:var(--ink)}
.nav .active{color:var(--teal)}
.search{left:838px;top:22px;width:200px;height:28px;border:1px solid var(--line);border-radius:14px;font-size:10px;color:var(--muted);padding:7px 14px}
.search svg{position:absolute;right:12px;top:8px}

/* hero */
.hero{left:0;top:108px;width:1200px;height:617px;clip-path:polygon(0 0,100% 0,100% 80%,0 100%);
  background:linear-gradient(135deg,#1d3f4d 0%,#17606c 45%,#0e3a48 100%)}
.hero-logo{left:0;top:140px;width:1200px;display:flex;justify-content:center;align-items:center;gap:16px}
.hero-logo .brand-mark{width:110px;height:110px;background:transparent;border:5px solid #fff}
.hero-logo .brand-name{color:#fff;font-size:64px;letter-spacing:6px}
.hero-title{left:0;top:268px;width:1200px;text-align:center;font-family:"Raleway",sans-serif;font-weight:600;font-size:31px;line-height:46px;color:#fff;letter-spacing:.5px}
.dots{left:512px;top:468px;display:flex;gap:6px}
.dots span{width:42px;height:4px;background:rgba(255,255,255,.9)}
.dots span.off{background:rgba(255,255,255,.35)}

/* services */
.service{top:870px;width:278px;height:305px;border:1px solid var(--line);background:#fff;text-align:center}
.service .icon{width:112px;height:112px;margin:34px auto 0;border:3px solid var(--navy);border-radius:50%;display:flex;align-items:center;justify-content:center}
.service h3{font-family:"Raleway",sans-serif;font-weight:700;font-size:14px;margin-top:28px;letter-spacing:.5px}
.service p{font-size:10.5px;line-height:19px;color:var(--muted);padding:0 30px;margin-top:10px}

/* feature bands */
.band{left:0;width:1200px;background:linear-gradient(90deg,#dcefee 0%,#cfe9ec 55%,#eaf4f6 100%)}
.photo{position:absolute}
.band-copy{width:560px}
.band-copy h2{font-family:"Raleway",sans-serif;font-weight:600;font-size:27px;letter-spacing:1px;color:var(--ink)}
.band-copy p{margin-top:18px;font-size:10.5px;line-height:22px;color:var(--muted)}

/* jobs */
.job{left:160px;width:880px;height:64px;background:#f1f3f4;border:1px solid #e3e7e9;display:flex;align-items:center;font-size:14.5px;color:var(--ink)}
.job .title{margin-left:38px;width:444px}
.job .loc{display:flex;align-items:center;gap:8px;font-size:11px;color:#8a959b;width:280px}
.tag{width:90px;height:28px;border-radius:14px;font-family:"Raleway",sans-serif;font-weight:700;font-size:10.5px;color:#fff;display:flex;align-items:center;justify-content:center}
.tag.full{background:var(--teal)}
.tag.part{background:var(--navy)}
.view-all{left:0;width:1200px;top:2480px;text-align:center;font-family:"Raleway",sans-serif;font-weight:700;font-size:13px;text-decoration:underline;letter-spacing:.5px}

/* contact */
.contact-bg{left:0;top:3230px;width:1200px;height:490px;clip-path:polygon(0 0,100% 0,100% 88%,0 100%);
  background:linear-gradient(180deg,#fff 0%,#e6f4f6 45%,#c9e8ec 100%)}
.field{left:327px;width:251px;height:28px;background:#fff;border:1px solid #b9c4c8;font-size:10px;color:var(--muted);padding:7px 8px}
.message{left:584px;top:3387px;width:286px;height:128px;background:#fff;border:1px solid #b9c4c8;font-size:10px;color:var(--muted);padding:7px 8px}

/* partners */
.partner{top:3852px;height:58px;background:#c9cfd2;border-radius:4px}

/* footer */
.site-footer{left:0;top:4065px;width:1200px;height:315px;background:var(--footer);color:#c7d0d5}
.foot-col{top:48px}
.foot-col h4{font-family:"Raleway",sans-serif;font-weight:600;font-size:17px;color:#fff;margin-bottom:16px}
.foot-col li{list-style:none;font-size:11px;line-height:23px}
.contact-list li{display:flex;align-items:center;gap:8px}
.foot-line{left:160px;top:242px;width:880px;height:1px;background:#2c3a44}
.copyright{left:160px;top:268px;font-size:10px;color:#9aa6ad}
.social{left:906px;top:260px;display:flex;gap:8px}
.social span{width:26px;height:26px;border-radius:50%;background:var(--teal)}
</style>
</head>
<body>

<header class="abs site-header">
  <div class="abs brand" style="left:160px;top:22px">
    <div class="brand-mark"></div>
    <div>
      <div class="brand-name">QUORVIX</div>
      <div class="brand-sub">CORE IT SYSTEMS</div>
    </div>
  </div>
  <div class="abs search">Zoek...
    <svg width="12" height="12" viewBox="0 0 12 12"><circle cx="5" cy="5" r="3.8" fill="none" stroke="#1f2a30" stroke-width="1.4"/><line x1="8" y1="8" x2="11" y2="11" stroke="#1f2a30" stroke-width="1.4"/></svg>
  </div>
  <nav class="abs nav"><span class="active">HOME</span><span>OUR SOLUTIONS</span><span>OUR TEAM</span><span>JOB</span><span>CONTACT</span></nav>
</header>

<section class="abs hero" role="img" aria-label="Team of colleagues meeting in a bright office, tinted teal"></section>
<div class="abs hero-logo">
  <div class="brand-mark"></div>
  <div class="brand-name">QUORVIX</div>
</div>
<h1 class="abs hero-title">WE SHARE OUR KNOWLEDGE<br>WITH CUSTOMERS</h1>
<div class="abs dots"><span></span><span></span><span class="off"></span><span></span></div>

<h2 class="section-title" style="top:748px">QUORVIX IT SERVICES</h2>
<p class="intro" style="top:796px">Sed ut perspiciatis unde omnis iste natus error sit voluptatem accusantium doloremque laudantium, totam rem aperiam, eaque ipsa quae ab illo inventore veritatis et quasi architecto beatae vitae dicta sunt explicabo. Nemo enim ipsam voluptatem.</p>

<article class="abs service" style="left:160px">
  <div class="icon"><svg width="50" height="50" viewBox="0 0 50 50" fill="none" stroke="#12303b" stroke-width="2.5"><rect x="14" y="8" width="30" height="22"/><circle cx="9" cy="18" r="4"/><path d="M5 44V28h10l8-6M12 44V34"/><path d="M22 30l-4 14M36 30l4 14"/></svg></div>
  <h3>TRAINING</h3>
  <p>Sed ut perspiciatis unde omnis iste na sit voluptatem accusantium doloremque, totam rem aperiam, eaque ipsa quae abo</p>
</article>
<article class="abs service" style="left:461px">
  <div class="icon"><svg width="50" height="50" viewBox="0 0 50 50" fill="none" stroke="#12303b" stroke-width="2.5"><circle cx="14" cy="12" r="5"/><circle cx="36" cy="26" r="5"/><path d="M5 30c0-7 4-10 9-10s9 3 9 10zM27 44c0-7 4-10 9-10s9 3 9 10z"/><path d="M28 8h14v10H28z"/></svg></div>
  <h3>PERSONAL COACHING</h3>
  <p>Sed ut perspiciatis unde omnis iste na sit voluptatem accusantium doloremque, totam rem aperiam, eaque ipsa quae abo</p>
</article>
<article class="abs service" style="left:762px">
  <div class="icon"><svg width="50" height="50" viewBox="0 0 50 50" fill="none" stroke="#12303b" stroke-width="2.5"><rect x="14" y="6" width="32" height="24"/><path d="M20 24v-6M27 24v-10M34 24v-4M40 24v-12"/><circle cx="9" cy="22" r="4"/><path d="M4 46V32h10l6-4M10 46V38"/></svg></div>
  <h3>EDUCATION TRAJECTS</h3>
  <p>Sed ut perspiciatis unde omnis iste na sit voluptatem accusantium doloremque, totam rem aperiam, eaque ipsa quae abo</p>
</article>

<section class="abs band" style="top:1255px;height:660px;clip-path:polygon(0 15%,100% 0,100% 90%,0 100%)">
  <div class="photo" role="img" aria-label="Smiling woman working on a laptop with a coffee cup" style="left:620px;top:0;width:580px;height:660px;background:linear-gradient(160deg,#b9d9df 0%,#8ec0c9 50%,#d6e8ea 100%)"></div>
</section>
<div class="abs band-copy" style="left:160px;top:1480px">
  <h2>ABOUT US</h2>
  <p>Sed ut perspiciatis unde omnis iste natus error sit voluptatem accusantium doloremque laudantium, totam rem aperiam, eaque ipsa quae ab illo inventore veritatis et quasi architecto beatae vitae dicta sunt explicabo. Nemo enim ipsam voluptatem quia voluptas sit aspernatur aut odit aut fugit, sed quia consequuntur magni dolores eos qui ratione voluptatem sequi nesciunt. Neque porro quisquam est, qui dolorem ipsum quia dolor sit amet, sed quia consequuntur magni dolores eos qui ratione voluptatem sequi nesciunt. Neque porro quisquam est, qui dolore.</p>
</div>
<div class="btn" style="left:160px;top:1704px;width:104px;height:30px">READ MORE</div>

<h2 class="section-title" style="top:1940px">JOB LISTING</h2>
<p class="intro" style="top:1990px">Sed ut perspiciatis unde omnis iste natus error sit voluptatem accusantium doloremque laudantium, totam rem aperiam, eaque ipsa quae ab illo inventore veritatis et quasi architecto beatae vitae dicta sunt explicabo. Nemo enim ipsam voluptatem.</p>

<div class="abs job" style="top:2065px"><span class="title">Sed ut perspiciatis unde omnis iste natus</span><span class="loc"><svg width="10" height="13" viewBox="0 0 10 13"><path d="M5 0a5 5 0 0 1 5 5c0 3-5 8-5 8S0 8 0 5a5 5 0 0 1 5-5z" fill="#1fa3a5"/><circle cx="5" cy="5" r="1.8" fill="#fff"/></svg>Location Name, City Name</span><span class="tag full">FULL TIME</span></div>
<div class="abs job" style="top:2140px"><span class="title">Sed ut perspiciatis unde omnis iste natus</span><span class="loc"><svg width="10" height="13" viewBox="0 0 10 13"><path d="M5 0a5 5 0 0 1 5 5c0 3-5 8-5 8S0 8 0 5a5 5 0 0 1 5-5z" fill="#1fa3a5"/><circle cx="5" cy="5" r="1.8" fill="#fff"/></svg>Location Name, City Name</span><span class="tag full">FULL TIME</span></div>
<div class="abs job" style="top:2216px"><span class="title">Sed ut perspiciatis unde omnis iste natus</span><span class="loc"><svg width="10" height="13" viewBox="0 0 10 13"><path d="M5 0a5 5 0 0 1 5 5c0 3-5 8-5 8S0 8 0 5a5 5 0 0 1 5-5z" fill="#1fa3a5"/><circle cx="5" cy="5" r="1.8" fill="#fff"/></svg>Location Name, City Name</span><span class="tag part">PART TIME</span></div>
<div class="abs job" style="top:2292px"><span class="title">Sed ut perspiciatis unde omnis iste natus</span><span class="loc"><svg width="10" height="13" viewBox="0 0 10 13"><path d="M5 0a5 5 0 0 1 5 5c0 3-5 8-5 8S0 8 0 5a5 5 0 0 1 5-5z" fill="#1fa3a5"/><circle cx="5" cy="5" r="1.8" fill="#fff"/></svg>Location Name, City Name</span><span class="tag full">FULL TIME</span></div>
<div class="abs job" style="top:2366px"><span class="title">Sed ut perspiciatis unde omnis iste natus</span><span class="loc"><svg width="10" height="13" viewBox="0 0 10 13"><path d="M5 0a5 5 0 0 1 5 5c0 3-5 8-5 8S0 8 0 5a5 5 0 0 1 5-5z" fill="#1fa3a5"/><circle cx="5" cy="5" r="1.8" fill="#fff"/></svg>Location Name, City Name</span><span class="tag part">PART TIME</span></div>
<div class="abs view-all">VIEW ALL JOBS</div>

<section class="abs band" style="top:2540px;height:670px;clip-path:polygon(0 15%,100% 0,100% 95%,0 100%);background:linear-gradient(90deg,#eef5f6 0%,#e7f1f3 50%,#dceef0 100%)">
  <div class="photo" role="img" aria-label="Smiling businesswoman holding a tablet near a window" style="left:0;top:0;width:540px;height:670px;background:linear-gradient(120deg,#cfe3e6 0%,#a9cdd3 55%,#e4eef0 100%)"></div>
</section>
<div class="abs band-copy" style="left:564px;top:2746px;width:480px">
  <h2>WHAT WE DO</h2>
  <p>Sed ut perspiciatis unde omnis iste natus error sit voluptatem accusantium doloremque laudantium, totam rem aperiam, eaque ipsa quae ab illo inventore veritatis et quasi architecto beatae vitae dicta sunt explicabo. Nemo enim ipsam voluptatem quia voluptas sit aspernatur aut odit aut fugit, sed quia consequuntur magni dolores eos qui ratione voluptatem sequi nesciunt. Neque porro quisquam est, qui dolorem ipsum quia dolor sit amet, aspernatur aut odit aut fugit, sed quia consequuntur magni dolores eos qui ratione voluptatem sequi nesciunt. Neque porro quisquam est, qui dolore.</p>
</div>
<div class="btn" style="left:564px;top:2976px;width:104px;height:30px">READ MORE</div>

<div class="abs contact-bg"></div>
<h2 class="section-title" style="top:3270px">CONTACT US</h2>
<p class="intro" style="top:3318px;left:330px;width:540px">Sed ut perspiciatis unde omnis iste natus error sit voluptatem accusantium doloremque laudanti um, totam rem aperiam, eaque ipsa quae ab illo inventore veritatis et quasi architecto.</p>
<div class="abs field" style="top:3387px">Name:</div>
<div class="abs field" style="top:3420px">Email:</div>
<div class="abs field" style="top:3454px">Phone:</div>
<div class="abs field" style="top:3487px">Job:</div>
<div class="abs message">Message:</div>
<div class="btn" style="left:488px;top:3533px;width:222px;height:42px;font-size:13px;border-radius:21px">CONTACT US QUICKLY</div>

<h2 class="section-title" style="top:3740px">PARTNERS</h2>
<p class="intro" style="top:3786px;left:330px;width:540px">Sed ut perspiciatis unde omnis iste natus error sit voluptatem accusantium doloremque laudanti um, totam rem aperiam, eaque ipsa quae ab illo inventore veritatis et quasi architecto.</p>
<div class="abs partner" style="left:305px;width:110px"></div>
<div class="abs partner" style="left:447px;width:104px"></div>
<div class="abs partner" style="left:592px;width:182px"></div>
<div class="abs partner" style="left:812px;width:94px"></div>

<footer class="abs site-footer">
  <div class="abs" style="left:160px;top:42px;width:210px;text-align:center">
    <div class="brand-mark" style="width:92px;height:92px;margin:0 auto;background:var(--teal-dark)"></div>
    <div class="brand-name" style="color:#fff;font-size:40px;margin-top:12px">QUORVIX</div>
    <div class="brand-sub">CORE IT SYSTEMS</div>
  </div>
  <div class="abs foot-col" style="left:488px">
    <h4>Information</h4>
    <ul><li>Sed ut perspiciatis</li><li>Unde omnis iste natus</li><li>Voluptatem accusan</li><li>Tsum doloremque</li><li>Haudantium</li></ul>
  </div>
  <div class="abs foot-col" style="left:710px">
    <h4>Links</h4>
    <ul><li>Sed ut perspiciatis</li><li>Unde omnis iste natus</li><li>Voluptatem accusan</li><li>Tsum doloremque</li><li>Haudantium</li></ul>
  </div>
  <div class="abs foot-col" style="left:911px">
    <h4>Contact</h4>
    <ul class="contact-list">
      <li><svg width="8" height="10" viewBox="0 0 10 13"><path d="M5 0a5 5 0 0 1 5 5c0 3-5 8-5 8S0 8 0 5a5 5 0 0 1 5-5z" fill="#1fa3a5"/></svg>Lindenhof 14,</li>
      <li style="padding-left:16px">3521 AB Utrecht</li>
      <li><svg width="9" height="9" viewBox="0 0 10 10"><path d="M2 0l2 2-1 2c1 2 2 3 4 4l2-1 1 2-2 1C4 10 0 6 0 2z" fill="#1fa3a5"/></svg>Phone: 030-5512840</li>
      <li><svg width="10" height="8" viewBox="0 0 10 8"><rect width="10" height="8" fill="#1fa3a5"/><path d="M0 0l5 4 5-4" stroke="#151f27" fill="none"/></svg>Email: info@quorvix.nl</li>
    </ul>
  </div>
  <div class="abs foot-line"></div>
  <div class="abs copyright">© 2018 Quorvix All rights are reserved. Privacy | Terms of use</div>
  <div class="abs social"><span></span><span></span><span></span><span></span></div>
</footer>

</body>
</html>
```